Halvorn Homes-Real Estate of the Future

Halvorn Homes is a Residential Real Estate company which specializes in buying and selling homes. We pride ourselves on service, expertise, and building relationships. I would like to do a Billboard Ad for a The Size is 14 feet (Height) x 48 feet (width) displaying our current motto for "Real Estate of the Future" We have launched new programs and working with leaders in our industy Brimlot and other tech companies and changing the way Real Estate is done in Las Vegas, NV. Its exciting and NEW so we want to get the word out. Color Scheme Red, White, Grey and maybe black. Logo is uploaded and so is a picture head shot. I would like to see options with my headshot and with out.

```html
<!DOCTYPE html>
<html lang="en">
<head>
<meta charset="utf-8">
<title>Halvorn Homes - Real Estate of the Future</title>
<link rel="stylesheet" href="https://fonts.googleapis.com/css2?family=Anton&family=Open+Sans:wght@400;600;700&display=swap">
<style>
  :root {
    --page-bg: #ececec;
    --white: #ffffff;
    --red: #d40d0d;
    --red-deep: #a80808;
    --black: #0a0a0a;
    --grey-light: #f2f2f2;
    --grey-mid: #c9c9c9;
    --ink: #111111;
  }
  html, body {
    margin: 0;
    padding: 0;
    width: 1079px;
    height: 1200px;
    overflow: hidden;
    background: var(--page-bg);
  }
  .billboard {
    position: absolute;
    left: 20px;
    top: 448px;
    width: 1167px;
    height: 340px;
    transform: scale(0.8903);
    transform-origin: top left;
    background: var(--white);
    box-shadow: 0 6px 18px rgba(0,0,0,0.25);
    overflow: hidden;
  }
  .billboard-shapes {
    position: absolute;
    inset: 0;
    width: 1167px;
    height: 340px;
  }
  .brand-name {
    position: absolute;
    left: 0;
    width: 300px;
    top: 152px;
    margin: 0;
    text-align: center;
    font-family: "Open Sans", sans-serif;
    font-weight: 600;
    font-size: 32px;
    color: var(--red);
    letter-spacing: 0.5px;
  }
  .headline {
    position: absolute;
    left: 350px;
    width: 460px;
    top: 22px;
    margin: 0;
    text-align: center;
    font-family: "Anton", sans-serif;
    font-weight: 400;
    color: var(--white);
    line-height: 1.15;
    text-shadow: 2px 2px 0 rgba(0,0,0,0.35);
  }
  .headline .line-one { display: block; font-size: 68px; }
  .headline .line-two { display: block; font-size: 74px; }
  .address {
    position: absolute;
    left: 406px;
    top: 200px;
    width: 348px;
    height: 20px;
    border: 1px solid var(--white);
    font-family: "Open Sans", sans-serif;
    font-weight: 600;
    font-size: 13px;
    line-height: 20px;
    color: var(--white);
    text-align: center;
  }
  .call-now {
    position: absolute;
    left: 315px;
    width: 480px;
    top: 232px;
    height: 60px;
    line-height: 60px;
    margin: 0;
    text-align: center;
    font-family: "Open Sans", sans-serif;
    font-weight: 700;
    font-size: 35px;
    color: var(--ink);
  }
  .website {
    position: absolute;
    left: 300px;
    width: 480px;
    top: 292px;
    height: 48px;
    line-height: 48px;
    margin: 0;
    text-align: center;
    font-family: "Open Sans", sans-serif;
    font-weight: 400;
    font-size: 22px;
    color: var(--white);
  }
  .website strong { font-weight: 700; }
</style>
</head>
<body>
  <section class="billboard" aria-label="Halvorn Homes billboard">
    <svg class="billboard-shapes" viewBox="0 0 1167 340" aria-hidden="false">
      <defs>
        <linearGradient id="redPanelFill" x1="0" y1="0" x2="0" y2="1">
          <stop offset="0" stop-color="var(--red)"/>
          <stop offset="1" stop-color="var(--red-deep)"/>
        </linearGradient>
        <linearGradient id="greyBandFill" x1="0" y1="0" x2="1" y2="0">
          <stop offset="0" stop-color="#bdbdbd"/>
          <stop offset="0.5" stop-color="#f7f7f7"/>
          <stop offset="1" stop-color="#bdbdbd"/>
        </linearGradient>
        <linearGradient id="portraitPanelFill" x1="0" y1="0" x2="1" y2="0">
          <stop offset="0" stop-color="#d2d2d2"/>
          <stop offset="0.45" stop-color="var(--grey-light)"/>
          <stop offset="1" stop-color="var(--grey-mid)"/>
        </linearGradient>
        <linearGradient id="portraitFill" x1="0" y1="0" x2="0" y2="1">
          <stop offset="0" stop-color="#e4e4e4"/>
          <stop offset="0.45" stop-color="#c9a48f"/>
          <stop offset="0.6" stop-color="#1f2a44"/>
          <stop offset="1" stop-color="#141b2e"/>
        </linearGradient>
      </defs>
      <polygon class="accent-wedge-top" points="300,0 380,0 338,190" fill="var(--black)"/>
      <polygon class="portrait-panel" points="845,0 1167,0 1167,340 770,340" fill="url(#portraitPanelFill)"/>
      <polygon class="headline-panel" points="378,0 845,0 770,340 302,340" fill="url(#redPanelFill)"/>
      <polygon class="call-band" points="326,232 794,232 781,292 313,292" fill="url(#greyBandFill)"/>
      <polygon class="accent-wedge-bottom" points="770,340 810,178 870,340" fill="var(--black)"/>
      <rect class="agent-headshot" x="870" y="30" width="297" height="310" rx="6" fill="url(#portraitFill)" role="img" aria-label="Headshot of the agent in a navy suit and blue shirt"/>
    </svg>

    <p class="brand-name">Halvorn Homes</p>

    <h1 class="headline">
      <span class="line-one">REAL ESTATE</span>
      <span class="line-two">OF THE FUTURE</span>
    </h1>

    <div class="address">218 W Sandmere Ave Ste 40, Henderson, NV, 89012</div>

    <p class="call-now">Call Now:702-555-0148</p>

    <p class="website">www.<strong>halvornhomesgroup</strong>.net</p>
  </section>
</body>
</html>
```